New emerging fitness company

A need a website to advertise my classes & personal training services. I also want a personal touch like showing where I started my own fitness journey.
I need a website where I can upload fitness programs for people to purchase. These will be in various formats like video & written based. I’m looking to have various online fitness programs for purchase either in one lump sum or a subscription. Also in the future products for sale like protein powders & other health products

Target Market(s)

Women aged 18-45, mostly

Industry/Entity Type

Fitness

Coding

Coded - Design and coding required

Number of Pages Required

5+ page

Font styles to use
Sans Serif

Colors
e667a6
e33f95
85acd3
82c8e6

Requirements
Must have
• The ability for people to log in & view exercise plans & programs. Also I’ll be loading these online via video. Must have the ability for clients to pay online. Be easy to use & navigate. Also must link to my logo that I have designed through make foundry

```html
<!DOCTYPE html>
<html lang="en">
<head>
<meta charset="utf-8">
<title>Vivid Form – Make Your Body Stronger</title>
<link rel="stylesheet" href="https://fonts.googleapis.com/css2?family=Lato:wght@400;700&family=Montserrat:wght@700&family=Roboto:wght@400;500;700&display=swap">
<style>
:root{
  --pink:#f03e96;
  --pink-soft:#e667a6;
  --dark:#141414;
  --footer:#1f1f1f;
  --slate:#474b52;
  --light:#f6f6f6;
  --white:#ffffff;
  --ink:#1b1b1b;
  --muted:#9a9a9a;
}
*{margin:0;padding:0;box-sizing:border-box}
html,body{width:701px;height:1200px;overflow:hidden;background:var(--white)}
body{font-family:"Lato",sans-serif;color:var(--ink)}
.canvas{position:relative;width:701px;height:1200px;overflow:hidden}
.abs{position:absolute}
.brand{display:flex;align-items:center;gap:3px;font-family:"Lato",sans-serif;font-weight:700;color:var(--pink);letter-spacing:.3px;white-space:nowrap}
.brand-mark{width:6px;height:6px;background:var(--pink)}

/* header */
.site-header{left:0;top:0;width:701px;height:34px;background:rgba(30,30,30,.82);z-index:3}
.site-header .brand{position:absolute;left:207px;top:11px;font-size:9px}
.nav{position:absolute;left:278px;top:11px;display:flex;gap:8px;font-family:"Roboto",sans-serif;font-size:4.4px;color:var(--white);white-space:nowrap}
.nav a{color:inherit;text-decoration:none}
.nav .active{color:var(--pink);border-bottom:1px dotted var(--pink);padding-bottom:1px}
.login-btn{left:429px;top:8px;width:40px;height:12px;border-radius:6px;background:var(--pink);color:var(--white);font-size:3.8px;display:flex;align-items:center;justify-content:center}
.search{left:478px;top:11px}
.lang{left:491px;top:12px;display:flex;gap:1px}
.lang span{width:6px;height:4px;display:block}

/* hero */
.hero{left:0;top:0;width:701px;height:220px;background:linear-gradient(100deg,#7a3a30 0%,#8c4536 35%,#6b3a34 60%,#2d2a2c 78%,#4a3a36 100%)}
.hero-kicker{left:0;width:701px;top:76px;text-align:center;font-size:5.2px;color:var(--white);letter-spacing:.3px}
.hero-title{left:0;width:701px;top:88px;text-align:center;font-family:"Montserrat",sans-serif;font-weight:700;font-size:19px;line-height:19.5px;color:var(--white);letter-spacing:1px}
.hero-btn{left:329px;top:137px;width:43px;height:12px;border:1px solid var(--pink);border-radius:6px;color:var(--pink);font-size:3.4px;display:flex;align-items:center;justify-content:center}
.round-arrow{width:23px;height:14px;border-radius:7px;background:var(--pink);display:flex;align-items:center;justify-content:center}
.hero-progress{left:0;top:219px;width:336px;height:1.5px;background:var(--pink)}

/* programs */
.programs{left:0;top:220px;width:701px;height:139px;background:var(--light)}
.section-title{font-family:"Roboto",sans-serif;font-weight:700;font-size:9.5px;letter-spacing:.1px}
.underline{width:8px;height:1.2px;background:var(--pink)}
.programs-text{left:198px;top:271px;width:96px;font-size:3.8px;line-height:6.6px;color:var(--pink)}
.small-arrow{width:19px;height:11px;border-radius:6px;background:var(--pink);display:flex;align-items:center;justify-content:center}
.program-card{top:248px;width:62px;height:83px;background:var(--white)}
.program-card .photo{width:100%;height:54px}
.program-card .tick{position:absolute;left:28px;top:53px;width:6px;height:1px;background:var(--pink)}
.program-card h3{position:absolute;top:63px;width:100%;text-align:center;font-family:"Roboto",sans-serif;font-weight:500;font-size:5px;line-height:6.4px}

/* dark section */
.dark{left:0;top:359px;width:701px;height:412px;background:var(--dark)}
.light-title{color:var(--white)}
.about-intro{left:198px;top:409px;width:155px;font-size:3.8px;line-height:6.6px;color:var(--white)}
.about-list{left:198px;top:427px;list-style:none;font-size:3.8px;color:var(--white)}
.about-list li{display:flex;align-items:center;gap:2px;height:12.1px}
.pill-btn{border-radius:7px;background:var(--pink);color:var(--white);display:flex;align-items:center;justify-content:center}
.about-photo{left:372px;top:387px;width:115px;height:144px;background:linear-gradient(180deg,#6a6a6a,#3f3f3f 60%,#2b2b2b)}
.center-head{left:0;width:701px;text-align:center}
.center-line{left:347px;width:8px;height:1.2px;background:var(--pink)}
.news-intro{left:0;width:701px;top:579px;text-align:center;font-size:3.8px;line-height:6.6px;color:var(--white)}
.news-card{top:605px;width:97px;height:141px;background:var(--light)}
.news-card .photo{width:100%;height:70px}
.date-badge{position:absolute;left:5px;top:4px;width:16px;height:16px;border-radius:50%;background:var(--pink);color:var(--white);text-align:center;font-size:5.4px;line-height:6px;padding-top:2.5px}
.date-badge small{display:block;font-size:2.4px;line-height:3px}
.news-card h3{position:absolute;left:5px;top:76px;font-family:"Roboto",sans-serif;font-weight:400;font-size:5.4px}
.news-meta{position:absolute;left:5px;top:84px;font-size:3px;color:var(--muted)}
.news-meta b{color:var(--pink);font-weight:400}
.news-card p{position:absolute;left:5px;top:95px;width:88px;font-size:3.6px;line-height:6.6px;color:var(--pink)}
.news-foot{position:absolute;left:4px;top:130px;width:89px;display:flex;justify-content:space-between;font-size:3.4px}
.news-foot span{background:var(--white);border-radius:4px;padding:1.5px 4px;color:var(--pink)}
.views{color:var(--muted)!important;display:flex;align-items:center;gap:1px}

/* pricing */
.pricing-intro{left:0;width:701px;top:819px;text-align:center;font-size:3.7px;line-height:6.6px;color:var(--pink)}
.price-card{top:845px;width:97px;height:153px}
.price-card svg{position:absolute;left:0;top:0}
.price-label{position:absolute;top:7px;width:100%;text-align:center;color:var(--white);font-size:4.8px;line-height:6px}
.price-amount{position:absolute;top:19px;width:100%;text-align:center;color:var(--white);font-size:13px;line-height:13px;font-weight:700}
.price-amount sup{font-size:7px;vertical-align:-1px;font-weight:400}
.price-period{position:absolute;top:35px;width:100%;text-align:center;color:var(--white);font-size:3.4px;line-height:4px}
.features{position:absolute;top:58px;width:100%;list-style:none;text-align:center;font-size:3.8px;color:var(--white)}
.features li{height:13.3px}
.details-btn{position:absolute;left:31px;top:133px;width:35px;height:12px;border-radius:6px;background:var(--light);color:var(--ink);font-size:3.6px;display:flex;align-items:center;justify-content:center}

/* footer */
.site-footer{left:0;top:1026px;width:701px;height:174px;background:var(--footer)}
.foot-head{font-family:"Roboto",sans-serif;font-weight:700;font-size:4.4px;color:var(--white)}
.social-box{left:198px;top:1076px;width:93px;height:35px;background:linear-gradient(90deg,#d9d6d3,#b8b2ad 45%,#e8e6e4)}
.social-box .name{position:absolute;left:18px;top:4px;font-size:5px;color:var(--white);font-family:"Roboto",sans-serif}
.social-box .likes{position:absolute;left:18px;top:10px;font-size:2.6px;color:var(--white)}
.social-box .thumb{position:absolute;left:3px;top:3px;width:14px;height:13px;border:1px solid var(--white);background:#8a7c74}
.social-box .btn{position:absolute;bottom:2px;height:5px;background:var(--white);font-size:2.6px;color:var(--ink);padding:0 2px;line-height:5px}
.foot-links{left:302px;top:1077px;list-style:none;font-size:4px;color:var(--muted)}
.foot-links li{height:15.4px}
.contact-text{left:407px;top:1077px;width:95px;font-size:4px;line-height:7px;color:var(--muted)}
.contact-row{left:407px;display:flex;align-items:center;gap:4px;font-size:4px;color:var(--muted)}
.foot-rule{left:198px;top:1142px;width:306px;height:1px;background:#333}
.copyright{left:304px;width:200px;top:1163px;text-align:right;font-size:4px;color:var(--white)}
.copyright b{font-weight:700}
.copyright span{color:var(--muted)}
</style>
</head>
<body>
<div class="canvas">

  <!-- hero -->
  <div class="abs hero" role="img" aria-label="Photo of a woman athlete leaning against a brick wall"></div>
  <header class="abs site-header">
    <div class="brand"><span class="brand-mark"></span>VIVID FORM</div>
    <nav class="nav">
      <a class="active">Home</a><a>About</a><a>Fitness Programs</a><a>Contact Us</a><a>News &amp; Events</a>
    </nav>
  </header>
  <div class="abs login-btn" style="z-index:4">USER LOG-IN</div>
  <svg class="abs search" style="z-index:4" width="5" height="5" viewBox="0 0 10 10"><circle cx="4" cy="4" r="3" fill="none" stroke="#fff" stroke-width="1.6"/><line x1="6.3" y1="6.3" x2="9" y2="9" stroke="#fff" stroke-width="1.6"/></svg>
  <div class="abs lang" style="z-index:4"><span style="background:#3a4a8c"></span><span style="background:#d8a43a"></span></div>

  <div class="abs hero-kicker">YOUR BODY FIT</div>
  <h1 class="abs hero-title">MAKE YOUR BODY<br>STRONGER</h1>
  <div class="abs hero-btn">GET STARTED</div>
  <div class="abs round-arrow" style="left:455px;top:189px"><svg width="7" height="4" viewBox="0 0 14 8"><path d="M14 4H2M5 1L1 4l4 3" fill="none" stroke="#fff" stroke-width="1.6"/></svg></div>
  <div class="abs round-arrow" style="left:481px;top:189px"><svg width="7" height="4" viewBox="0 0 14 8"><path d="M0 4h12M9 1l4 3-4 3" fill="none" stroke="#fff" stroke-width="1.6"/></svg></div>
  <div class="abs hero-progress"></div>

  <!-- programs -->
  <section class="abs programs"></section>
  <h2 class="abs section-title" style="left:198px;top:247px">FITNESS PROGRAMS</h2>
  <div class="abs underline" style="left:198px;top:259px"></div>
  <p class="abs programs-text">Explore a different way to travel. This isot as hop's version of Lorem Ipsum. oin gra travel. This isot as hop's version of Lorem Ipsum. oin gra nibh auctor aliquet. nean sollicin, lorem quis.</p>
  <div class="abs small-arrow" style="left:198px;top:306px"><svg width="6" height="4" viewBox="0 0 14 8"><path d="M14 4H2M5 1L1 4l4 3" fill="none" stroke="#fff" stroke-width="1.8"/></svg></div>
  <div class="abs small-arrow" style="left:220px;top:306px"><svg width="6" height="4" viewBox="0 0 14 8"><path d="M0 4h12M9 1l4 3-4 3" fill="none" stroke="#fff" stroke-width="1.8"/></svg></div>

  <article class="abs program-card" style="left:303px">
    <div class="photo" role="img" aria-label="Boxer in gloves against a dark wall" style="background:linear-gradient(135deg,#3a3a3a,#6b6b6b 50%,#2e2e2e)"></div>
    <span class="tick"></span><h3>BOXING AND<br>KICKBOXING</h3>
  </article>
  <article class="abs program-card" style="left:372px">
    <div class="photo" role="img" aria-label="Woman stretching on a running track" style="background:linear-gradient(180deg,#8a8f96,#5a5d62 60%,#3c3d40)"></div>
    <span class="tick"></span><h3>RUNNING AND<br>STRETCHING</h3>
  </article>
  <article class="abs program-card" style="left:443px">
    <div class="photo" role="img" aria-label="Woman resting after a swim workout" style="background:linear-gradient(135deg,#8d8581,#c4bcb7 50%,#6f6663)"></div>
    <span class="tick"></span><h3>SWIMMING AND<br>HYDROGINASTICS</h3>
  </article>

  <!-- about + news -->
  <section class="abs dark"></section>
  <h2 class="abs section-title light-title" style="left:198px;top:387px">ABOUT MARA DELLING</h2>
  <div class="abs underline" style="left:198px;top:398px"></div>
  <p class="abs about-intro">Lorem Ipsum is simply dummy text of the printing and typesetting industry. Lorem Ipsum has been the industry's standard dummy text ever since the 1500s.</p>
  <ul class="abs about-list">
    <li><svg width="4" height="4" viewBox="0 0 10 10"><path d="M1 5l3 3 5-6" fill="none" stroke="#f03e96" stroke-width="2"/></svg>Magnis dis parturient montes, nascetur ridiculus mus.</li>
    <li><svg width="4" height="4" viewBox="0 0 10 10"><path d="M1 5l3 3 5-6" fill="none" stroke="#f03e96" stroke-width="2"/></svg>Aenean sollicitudin, lorem quis bibendum auctor, nisi elit consequat</li>
    <li><svg width="4" height="4" viewBox="0 0 10 10"><path d="M1 5l3 3 5-6" fill="none" stroke="#f03e96" stroke-width="2"/></svg>variations of passages There are many of Lorem.</li>
    <li><svg width="4" height="4" viewBox="0 0 10 10"><path d="M1 5l3 3 5-6" fill="none" stroke="#f03e96" stroke-width="2"/></svg>Magnis dis parturient montes, nascetur ridiculus mus.</li>
    <li><svg width="4" height="4" viewBox="0 0 10 10"><path d="M1 5l3 3 5-6" fill="none" stroke="#f03e96" stroke-width="2"/></svg>Elit. Duis se Nec sagittis sem nibh idd odio sit amet akshay.</li>
  </ul>
  <div class="abs pill-btn" style="left:198px;top:491px;width:46px;height:13px;font-size:4px">KNOW MORE</div>
  <div class="abs about-photo" role="img" aria-label="Trainer working with battle ropes in front of a metal shutter"></div>

  <h2 class="abs section-title light-title center-head" style="top:557px">NEWS &amp; EVENTS</h2>
  <div class="abs center-line" style="top:568px"></div>
  <p class="abs news-intro">Lorem Ipsum is simply dummy text of the printing and typesetting industry. Lorem Ipsum<br>has been the industry's standard dummy text ever since the 1500s.</p>

  <article class="abs news-card" style="left:198px">
    <div class="photo" role="img" aria-label="Smiling woman lifting dumbbells in a group class" style="background:linear-gradient(135deg,#f0ece4,#d9cfc2 50%,#b9a99b)"></div>
    <div class="date-badge">12<small>SEP</small></div>
    <h3>Body Compact</h3>
    <div class="news-meta"><b>SUPER USER</b> &nbsp;| &nbsp;BLOG GYM</div>
    <p>Sollicitudin, lorem quis bibe u auctor, nisi elit couat ipsu, nec sagittis sem ni id elit. Duis sed odio sit amet nibh vulpute cursus. Proin gravida nibh vel velit tor aliquet. This is Lorem's...</p>
    <div class="news-foot"><span class="views"><svg width="4" height="3" viewBox="0 0 10 6"><ellipse cx="5" cy="3" rx="4.5" ry="2.6" fill="none" stroke="#f03e96"/><circle cx="5" cy="3" r="1.2" fill="#f03e96"/></svg>14</span><span>READ MORE</span></div>
  </article>
  <article class="abs news-card" style="left:302px">
    <div class="photo" role="img" aria-label="Athlete curling a dumbbell against a grey wall" style="background:linear-gradient(135deg,#6a6a6a,#4a4a4a 50%,#7d7d7d)"></div>
    <div class="date-badge">12<small>SEP</small></div>
    <h3>Dance Fitness</h3>
    <div class="news-meta"><b>SUPER USER</b> &nbsp;| &nbsp;BLOG GYM</div>
    <p>Sollicitudin, lorem quis bibe u auctor, nisi elit couat ipsu, nec sagittis sem ni id elit. Duis sed odio sit amet nibh vulpute cursus. Proin gravida nibh vel velit tor aliquet. This is Lorem's...</p>
    <div class="news-foot"><span class="views"><svg width="4" height="3" viewBox="0 0 10 6"><ellipse cx="5" cy="3" rx="4.5" ry="2.6" fill="none" stroke="#f03e96"/><circle cx="5" cy="3" r="1.2" fill="#f03e96"/></svg>7</span><span>READ MORE</span></div>
  </article>
  <article class="abs news-card" style="left:407px">
    <div class="photo" role="img" aria-label="Woman doing a dumbbell row in a gym" style="background:linear-gradient(135deg,#c9a27e,#8a5a4a 50%,#c74a5a)"></div>
    <div class="date-badge">12<small>SEP</small></div>
    <h3>Running Practice</h3>
    <div class="news-meta"><b>SUPER USER</b> &nbsp;| &nbsp;BLOG GYM</div>
    <p>Sollicitudin, lorem quis bibe u auctor, nisi elit couat ipsu, nec sagittis sem ni id elit. Duis sed odio sit amet nibh vulpute cursus. Proin gravida nibh vel velit tor aliquet. This is Lorem's...</p>
    <div class="news-foot"><span class="views"><svg width="4" height="3" viewBox="0 0 10 6"><ellipse cx="5" cy="3" rx="4.5" ry="2.6" fill="none" stroke="#f03e96"/><circle cx="5" cy="3" r="1.2" fill="#f03e96"/></svg>14</span><span>READ MORE</span></div>
  </article>

  <!-- pricing -->
  <h2 class="abs section-title center-head" style="top:797px">OUR PRICING TABLE</h2>
  <div class="abs center-line" style="top:808px"></div>
  <p class="abs pricing-intro">Explore a different way to travel. This isot as hop's version of Lorem Ipsum. oin gra of Lorem<br>Ipsum. oin gra at nisl malesuada pariatsunt in culpa qui offi.</p>

  <div class="abs price-card" style="left:198px">
    <svg width="97" height="153" viewBox="0 0 97 153"><path d="M0 19Q0 0 19 0H97V67H0Z" fill="#f03e96"/><path d="M0 67Q0 48 19 48H78Q97 48 97 29V134Q97 153 78 153H0Z" fill="#474b52"/></svg>
    <div class="price-label">STANDARD</div>
    <div class="price-amount"><sup>$</sup>199</div>
    <div class="price-period">PER MONTH</div>
    <ul class="features"><li>Free hand class</li><li>Gym Fintness</li><li>Running Practice</li><li>...</li><li>...</li></ul>
    <div class="details-btn">DETAILS !</div>
  </div>
  <div class="abs price-card" style="left:302px">
    <svg width="97" height="153" viewBox="0 0 97 153"><path d="M0 19Q0 0 19 0H97V67H0Z" fill="#f03e96"/><path d="M0 67Q0 48 19 48H78Q97 48 97 29V134Q97 153 78 153H0Z" fill="#474b52"/></svg>
    <div class="price-label">STANDARD</div>
    <div class="price-amount"><sup>$</sup>199</div>
    <div class="price-period">PER MONTH</div>
    <ul class="features"><li>Free hand class</li><li>Gym Fintness</li><li>Running Practice</li><li>Yoga Class</li><li>...</li></ul>
    <div class="details-btn">DETAILS !</div>
  </div>
  <div class="abs price-card" style="left:407px">
    <svg width="97" height="153" viewBox="0 0 97 153"><path d="M0 19Q0 0 19 0H97V67H0Z" fill="#f03e96"/><path d="M0 67Q0 48 19 48H78Q97 48 97 29V134Q97 153 78 153H0Z" fill="#474b52"/></svg>
    <div class="price-label">STANDARD</div>
    <div class="price-amount"><sup>$</sup>199</div>
    <div class="price-period">PER MONTH</div>
    <ul class="features"><li>Free hand class</li><li>Gym Fintness</li><li>Running Practice</li><li>Yoga Class</li><li>Aerobic Class</li></ul>
    <div class="details-btn">DETAILS !</div>
  </div>

  <!-- footer -->
  <footer class="abs site-footer"></footer>
  <h4 class="abs foot-head" style="left:198px;top:1054px">SOCIAL</h4>
  <div class="abs underline" style="left:198px;top:1063px"></div>
  <h4 class="abs foot-head" style="left:302px;top:1054px">COMPANY</h4>
  <div class="abs underline" style="left:302px;top:1063px"></div>
  <h4 class="abs foot-head" style="left:407px;top:1054px">CONTACT US</h4>
  <div class="abs underline" style="left:407px;top:1063px"></div>

  <div class="abs social-box" role="img" aria-label="Page preview with a cover photo of a woman stretching">
    <span class="thumb"></span>
    <span class="name">Vivid Form</span>
    <span class="likes">61 likes</span>
    <span class="btn" style="left:3px">Like Page</span>
    <span class="btn" style="right:3px">Share</span>
  </div>

  <ul class="abs foot-links"><li>Coaches</li><li>Mission</li><li>Strategy</li><li>Works</li></ul>

  <p class="abs contact-text">Phasellus placerat rutrum tristique. In hacse platea dictumst.</p>
  <div class="abs contact-row" style="top:1097px"><svg width="4" height="4" viewBox="0 0 10 10"><path d="M2 1l2 2-1 1.5q1 2 3 3L7.5 6.5l2 2L8 10Q1 8 0 2Z" fill="#f03e96"/></svg>+61 400 555 012</div>
  <div class="abs contact-row" style="top:1111px"><svg width="3" height="4" viewBox="0 0 8 10"><path d="M4 0a4 4 0 0 1 4 4c0 3-4 6-4 6S0 7 0 4a4 4 0 0 1 4-4z" fill="#f03e96"/></svg>48 Harbour Lane VIC 3000- Australia</div>
  <div class="abs contact-row" style="top:1129px"><svg width="4" height="3" viewBox="0 0 10 7"><rect width="10" height="7" fill="#f03e96"/><path d="M0 0l5 4 5-4" fill="none" stroke="#1f1f1f"/></svg>hello@vividform.fit</div>

  <div class="abs foot-rule"></div>
  <div class="abs brand" style="left:199px;top:1161px;font-size:14px"><span class="brand-mark" style="width:9px;height:9px"></span>VIVID FORM</div>
  <p class="abs copyright">2020 <b>Vivid Form</b> - All rights reserved. Design By: <span>Northline Studio</span>.</p>

</div>
</body>
</html>
```